Business Card Design Project

We need a business card for our IT services provider business. We provide services to small and medium business, and would like something that reflects the color scheme / branding on our recently updated website - www.larkbyte.com.au

The card type we have chosen is a matte laminated double sided configuration at 86mm x 54mm on 350 GSM cardboard.
Updates

Target Market(s)

Small and Medium Business owners

Industry/Entity Type

Business

Requirements
Must have
• *Details on all cards*

Company Name: LarkByte IT Pty Ltd
ABN: 62 385 219 604
Address: 47-49 Marrow Street, Kelbrook Vale, Victoria 3871
Phone: 1300 LARK BY
Fax: 03 9417 6209
Website: www.larkbyte.com.au
Logo/Handprint Icon

*Person Specific*

```html
<!DOCTYPE html>
<html lang="en">
<head>
<meta charset="utf-8">
<title>LarkByte IT – Business Card</title>
<link rel="stylesheet" href="https://fonts.googleapis.com/css2?family=Arimo:wght@400;700&display=swap">
<style>
  :root {
    --page-bg: #e4e6e9;
    --card-white: #f4f5f6;
    --brand-blue: #1a5a94;
    --ink: #1d1d1f;
    --on-blue: #e9edf2;
  }
  * { box-sizing: border-box; margin: 0; padding: 0; }
  html, body { width: 1200px; height: 984px; overflow: hidden; }
  body {
    background: var(--page-bg);
    font-family: "Arimo", Arial, sans-serif;
    color: var(--ink);
    display: flex;
    flex-direction: column;
    align-items: center;
    justify-content: center;
    gap: 40px;
  }
  .card {
    position: relative;
    width: 700px;
    height: 440px;
    box-shadow: 0 6px 18px rgba(0,0,0,0.18);
    overflow: hidden;
  }

  /* Back side */
  .card-back { background: var(--brand-blue); }
  .back-wordmark {
    position: absolute;
    left: 60px;
    top: 110px;
    font-size: 78px;
    font-weight: 400;
    color: var(--on-blue);
    letter-spacing: 1px;
  }
  .back-url {
    position: absolute;
    right: 40px;
    bottom: 150px;
    font-size: 22px;
    letter-spacing: 2px;
    color: var(--on-blue);
  }
  .back-url strong { font-weight: 700; }

  /* Front side */
  .card-front { background: var(--card-white); }
  .front-wordmark {
    position: absolute;
    left: 120px;
    top: 58px;
    font-size: 50px;
    font-weight: 400;
    color: var(--ink);
    letter-spacing: 1px;
  }
  .person {
    position: absolute;
    left: 50px;
    top: 176px;
    font-size: 17px;
    line-height: 1.32;
  }
  .person-name {
    font-weight: 700;
    color: var(--brand-blue);
    font-size: 19px;
    letter-spacing: 0.5px;
  }
  .divider {
    position: absolute;
    left: 372px;
    top: 226px;
    width: 3px;
    height: 170px;
    background: var(--brand-blue);
  }
  .company {
    position: absolute;
    left: 398px;
    top: 232px;
    font-size: 17px;
    line-height: 1.3;
  }
  .company-name {
    font-weight: 700;
    color: var(--brand-blue);
    font-size: 18px;
  }
  .contact-line {
    display: flex;
    align-items: center;
    gap: 12px;
  }
  .contact-line svg { width: 16px; height: 16px; fill: var(--brand-blue); flex: none; }
  .contact-line.first { margin-top: 6px; }
</style>
</head>
<body>

  <section class="card card-back" aria-label="Business card, back">
    <div class="back-wordmark">LarkByte IT</div>
    <div class="back-url">www.<strong>larkbyte</strong>.com.au</div>
  </section>

  <section class="card card-front" aria-label="Business card, front">
    <div class="front-wordmark">LarkByte IT</div>

    <div class="person">
      <div class="person-name">MARCUS HALE</div>
      <div>1300 482 917</div>
      <div>marcus@larkbyte.com.au</div>
    </div>

    <div class="divider"></div>

    <div class="company">
      <div class="company-name">LarkByte IT Pty Ltd</div>
      <div>ABN: 62 385 219 604</div>
      <div>47-49 Marrow Street,</div>
      <div>Kelbrook Vale, Victoria 3871</div>
      <div class="contact-line first">
        <svg viewBox="0 0 16 16" aria-label="Phone"><rect x="1" y="5" width="14" height="10" rx="1.5"/><rect x="3" y="1" width="10" height="4" rx="1"/><rect x="4" y="7" width="8" height="1.5" fill="#f4f5f6"/></svg>
        <span>1300 LARK BY</span>
      </div>
      <div class="contact-line">
        <svg viewBox="0 0 16 16" aria-label="Fax"><rect x="4" y="1" width="8" height="5"/><rect x="1" y="6" width="14" height="7" rx="1.5"/><rect x="4" y="11" width="8" height="4" fill="#1a5a94" stroke="#f4f5f6" stroke-width="1"/></svg>
        <span>03 9417 6209</span>
      </div>
    </div>
  </section>

</body>
</html>
```